Flyer für Unternehmensberatung
Es hat alles hervorragend geklappt, die Kommunikation lief Problemlos und die Änderungswünsche wurden absolut klasse umgesetzt. Wirklich toll. Ich bin total begeistert.
Zielgruppe
Ich berate kleine und mittelständische Unternehmen bei deren Zielgruppe, Dataenanalysen, SEA und Mediabuchung
Aufgabenstellung
Ich habe bestimmte farben und möchte auch Bilder von mir verwenden. Die Pakete sollen dargestellt werden. Gerne 2 Seiten, kurz und bündig. Ich möchte den Flyer auch digital per Mail versenden können.

```html
<!DOCTYPE html>
<html lang="de">
<head>
<meta charset="utf-8">
<title>Quirbalt Marketing – Flyer</title>
<link rel="stylesheet" href="https://fonts.googleapis.com/css2?family=Lexend:wght@300;400;500;600;700&display=swap">
<style>
  :root{
    --teal:#0b6e69;
    --teal-dark:#03504d;
    --gold:#d3b24f;
    --mint:#c3dedb;
    --ink:#555a5a;
    --paper:#ffffff;
    --stage:#808080;
    --sand-1:#f3ebe6;
    --sand-2:#ecd3b5;
  }
  *{margin:0;padding:0;box-sizing:border-box}
  html,body{width:1200px;height:1117px;overflow:hidden}
  body{background:var(--stage);font-family:"Lexend",sans-serif;position:relative}
  .page{position:absolute;top:173px;width:546px;height:772px;background:var(--paper);overflow:hidden}
  .page--front{left:40px}
  .page--back{left:614px}
  .abs{position:absolute;z-index:2}
  .page svg.waves{position:absolute;left:0;top:0;width:546px;height:772px}

  /* front */
  .backdrop{left:0;top:0;width:546px;height:260px;background:linear-gradient(90deg,var(--sand-1),#f1e2d2 50%,var(--sand-2));z-index:0}
  .portrait{border-radius:90px 90px 0 0;z-index:1}
  .portrait--front{left:261px;top:14px;width:260px;height:388px;background:linear-gradient(180deg,#a04a2e 0%,#d9a88c 22%,#2f6f93 38%,#245a7a 100%)}
  .brand{left:46px;top:38px;color:var(--teal);font-weight:500;font-size:27px;line-height:31px;letter-spacing:1px}
  .tagline{left:46px;top:118px;font-size:9.5px;color:#222;font-weight:400}
  .quote{left:46px;top:232px;width:220px;color:#fff;font-weight:600;font-size:23px;line-height:29.5px}
  .quote-author{left:46px;top:362px;color:var(--gold);font-weight:600;font-size:16px}
  .about-title{left:0;width:546px;top:430px;text-align:center;color:var(--gold);font-weight:600;font-size:44px;line-height:56px}
  .about-lead{left:50px;top:496px;width:456px;color:var(--teal);font-weight:600;font-size:9.6px;line-height:13.7px}
  .about-col{top:580px;width:222px;color:var(--ink);font-weight:300;font-size:10px;line-height:15.5px}
  .about-col--1{left:50px}
  .about-col--2{left:283px;width:225px}
  .url-tab{left:158px;top:726px;width:230px;height:46px;background:var(--mint);border-radius:12px 12px 0 0;display:flex;align-items:center;justify-content:center;gap:8px;color:var(--teal);font-weight:600;font-size:13px}

  /* back */
  .intro-box{left:46px;top:0;width:453px;height:106px;background:var(--mint);border-radius:0 0 12px 12px;display:flex;align-items:center;justify-content:center;text-align:center;color:var(--teal-dark);font-weight:600;font-size:15.5px;line-height:20px;padding:8px 14px 0}
  .back-backdrop{left:0;top:300px;width:546px;height:472px;background:linear-gradient(180deg,#fff 0%,#f7ede3 35%,var(--sand-2) 100%);z-index:0}
  .section-title{color:var(--teal);font-weight:600;font-size:14.5px;line-height:17px}
  .item{display:flex;gap:0;font-weight:300;font-size:9.6px;line-height:13.5px;color:var(--ink)}
  .item b{color:var(--gold);font-weight:600;width:24px;flex:none}
  .packages{left:65px;top:218px;width:202px;list-style:none}
  .packages li{height:20px;margin-bottom:7.5px;border:1.5px solid var(--gold);border-radius:10px;display:flex;align-items:center;gap:7px;padding-left:6px;font-size:9.8px;font-weight:600;color:#3d4242;background:#fff}
  .tick{width:10px;height:10px;flex:none}
  .portrait--back{left:258px;top:391px;width:288px;height:381px;border-radius:110px 0 0 0;background:linear-gradient(180deg,#a85232 0%,#e2b49a 28%,#f0c43e 45%,#e9b930 100%)}
  .cta-title{left:46px;top:553px;width:200px;color:var(--gold);font-weight:600;font-size:20px;line-height:23px}
  .cta-text{left:46px;top:606px;width:205px;color:#fff;font-weight:600;font-size:12px;line-height:16.4px}
  .cta-brand{left:46px;top:659px;color:var(--gold);font-weight:600;font-size:19px;line-height:28px;white-space:nowrap}
  .contact{left:46px;top:690px;list-style:none;color:#fff;font-size:10px;font-weight:300;letter-spacing:-.2px}
  .contact li{display:flex;align-items:center;gap:12px;height:19.3px;white-space:nowrap}
  .contact li.web{font-weight:600}
  .dot{width:10px;height:10px;flex:none}
</style>
</head>
<body>

<section class="page page--front">
  <div class="abs backdrop" role="img" aria-label="Hintergrund: heller Vorhang in Creme- und Sandtönen"></div>
  <svg class="waves" viewBox="0 0 546 772" aria-hidden="true">
    <defs>
      <linearGradient id="tealFront" x1="0" x2="1" y1="0" y2="0">
        <stop offset="0" stop-color="#0b6e69"/><stop offset="1" stop-color="#03504d"/>
      </linearGradient>
    </defs>
    <path d="M0 117 Q210 245 546 202 L546 772 L0 772Z" fill="var(--gold)"/>
    <path d="M0 143 Q220 262 546 212 L546 772 L0 772Z" fill="url(#tealFront)"/>
  </svg>
  <div class="abs portrait portrait--front" role="img" aria-label="Porträtfoto der Beraterin in blauer Bluse mit verschränkten Armen"></div>
  <svg class="waves" viewBox="0 0 546 772" aria-hidden="true" style="z-index:1">
    <path d="M0 472 Q273 330 546 416 L546 772 L0 772Z" fill="var(--gold)"/>
    <path d="M0 482 Q273 360 546 449 L546 772 L0 772Z" fill="var(--paper)"/>
  </svg>

  <div class="abs brand">QUIRBALT<br>MARKETING</div>
  <p class="abs tagline">Wir bringen Ihr Marketing auf den Punkt</p>

  <p class="abs quote">Der Köder muss dem Fisch schmecken, nicht dem Angler.</p>
  <p class="abs quote-author">Anselm Brückner</p>

  <h1 class="abs about-title">über mich</h1>
  <p class="abs about-lead">Ich bin Lena Quirbalt und unterstütze Sie dabei, ihre potenziellen Kunden zu analysieren und zielgerichtet anzusprechen. Nach über 15 Jahren Erfahrung im Marketing bei Kunden und Agenturen ist mir ist immer wieder aufgefallen, das oft Marketingkampagnen umgesetzt werden, ohne die Zielgruppe genau zu kennen und diese in der passenden Sprache anzusprechen.</p>
  <p class="abs about-col about-col--1">Der Spruch klingt sehr simple, beinhaltet aber die meistgemachten Fehler. Aber wie finden Sie den Köder, der Ihren Kunden schmeckt und nicht sofort nach Marketing aussieht? Vor allem wenn Sie, ganz andere Dinge mögen? Und sie nicht mehre tausend eure in teure Analysen und BeraterInnen investieren können?</p>
  <p class="abs about-col about-col--2">Genau dafür biete Ich Ihnen feste Pakete an, über die Sie ihre Zielgruppe analysieren können, Mediakanäle filtern können in denen sich ihre Zielgruppe aufhält, bis hin zur Unterstützung der geeigneten Videos auf Clipwelt zum Beispiel, um ihr unternehmen passend, aber auch zugeschnitten auf die Zielgruppe darstellen zu können</p>

  <div class="abs url-tab">
    <svg class="dot" viewBox="0 0 12 12" aria-hidden="true"><circle cx="6" cy="6" r="5" fill="none" stroke="var(--teal)" stroke-width="1.3"/><path d="M1 6h10M6 1c-2.5 3-2.5 7 0 10M6 1c2.5 3 2.5 7 0 10" fill="none" stroke="var(--teal)" stroke-width="1"/></svg>
    www.quirbalt-marketing.de
  </div>
</section>

<section class="page page--back">
  <div class="abs back-backdrop" role="img" aria-label="Hintergrund: heller Vorhang in Creme- und Sandtönen"></div>
  <svg class="waves" viewBox="0 0 546 772" aria-hidden="true">
    <defs>
      <linearGradient id="tealBack" x1="0" x2="1" y1="0" y2="0">
        <stop offset="0" stop-color="#0b6e69"/><stop offset="1" stop-color="#03504d"/>
      </linearGradient>
    </defs>
    <path d="M0 451 Q230 560 546 536 L546 772 L0 772Z" fill="var(--gold)"/>
    <path d="M0 478 Q240 578 546 551 L546 772 L0 772Z" fill="url(#tealBack)"/>
  </svg>
  <div class="abs portrait portrait--back" role="img" aria-label="Foto der Beraterin in gelbem Pullover beim Telefonieren"></div>

  <div class="abs intro-box">Teilen Sie mir mit, wobei Sie Unterstützung benötigen, wo Ihre Themen liegen und auf welche Marketingfragen sie eine Antwort benötigen.</div>

  <h2 class="abs section-title" style="left:46px;top:127px">Wählen sie direkt ein Paket aus</h2>
  <p class="abs item" style="left:46px;top:155px;width:225px"><b>A.</b><span>Wenn Sie genau wissen, was sie brauchen und wo Sie Unterstützung benötigen können Sie auch direkt eines der Pakete zum Festpreis buchen</span></p>
  <ul class="abs packages">
    <li><svg class="tick" viewBox="0 0 10 10" aria-hidden="true"><circle cx="5" cy="5" r="5" fill="var(--gold)"/><path d="M2.8 5.2l1.5 1.5 3-3" fill="none" stroke="#fff" stroke-width="1.3"/></svg>Zielgruppenanlayse Paket S/M/L</li>
    <li><svg class="tick" viewBox="0 0 10 10" aria-hidden="true"><circle cx="5" cy="5" r="5" fill="var(--gold)"/><path d="M2.8 5.2l1.5 1.5 3-3" fill="none" stroke="#fff" stroke-width="1.3"/></svg>Touchpointanalyse S/M/L</li>
    <li><svg class="tick" viewBox="0 0 10 10" aria-hidden="true"><circle cx="5" cy="5" r="5" fill="var(--gold)"/><path d="M2.8 5.2l1.5 1.5 3-3" fill="none" stroke="#fff" stroke-width="1.3"/></svg>SEA, Suchmaschinenmarketing</li>
    <li><svg class="tick" viewBox="0 0 10 10" aria-hidden="true"><circle cx="5" cy="5" r="5" fill="var(--gold)"/><path d="M2.8 5.2l1.5 1.5 3-3" fill="none" stroke="#fff" stroke-width="1.3"/></svg>Mediaplanung und Buchung</li>
  </ul>

  <h2 class="abs section-title" style="left:46px;top:344px;width:230px">Ich analysiere Ihre individuellen Zielgruppen</h2>
  <p class="abs item" style="left:46px;top:388px;width:225px"><b>B.</b><span>Die Zielgruppe ist das Wichtigste im Marketing. Wenn ich nicht weiß, wen ich ansprechen muss, kann ich das auch nicht zielgerichtet tun. Dabei helfe ich und wir finden Punktgenau ihre Zielgruppe</span></p>

  <h2 class="abs section-title" style="left:298px;top:127px">Ich optimiere ihr Marketing</h2>
  <p class="abs item" style="left:298px;top:154px;width:212px"><b>C.</b><span>Wenn die Zielgruppe bekannt, kann Ihr Marketing zielgerichtet ausgesteuert werden. Besonders die digitalen Kanäle stellen da oft noch eine Hürde da. Lassen Sie uns die gemeinsam nehmen und Ihr Marketing auf ein neues Level heben.</span></p>

  <h2 class="abs section-title" style="left:298px;top:278px;width:210px">Erhöhen wir Ihre Reichweite und Ihren Erfolg</h2>
  <p class="abs item" style="left:298px;top:320px;width:212px"><b>D.</b><span>Die richtige Zielgruppe passgenau und effizient ansprechen - das wollen wir zusammen erreichen, sodass sie einen spürbaren Erfolg verbuchen können.</span></p>

  <h2 class="abs cta-title">Sind Sie neugierig geworden?</h2>
  <p class="abs cta-text">Lassen Sie uns sprechen.<br>Ich berate Sie gern und freue mich auf Ihre Nachricht</p>
  <p class="abs cta-brand">Quirbalt Marketing</p>
  <ul class="abs contact">
    <li><svg class="dot" viewBox="0 0 10 10" aria-hidden="true"><circle cx="5" cy="5" r="5" fill="var(--gold)"/><path d="M3 2.6c.4-.3.8-.2 1 .2l.4.8c.1.3 0 .5-.2.7l-.3.2c.3.8.8 1.3 1.5 1.6l.3-.3c.2-.2.5-.2.7-.1l.8.5c.3.2.4.6.1.9-.5.6-1.2.7-1.9.3C4.5 6.7 3.4 5.6 2.8 4.3c-.3-.7-.2-1.3.2-1.7z" fill="var(--teal)"/></svg>0176-48291037</li>
    <li><svg class="dot" viewBox="0 0 10 10" aria-hidden="true"><circle cx="5" cy="5" r="5" fill="var(--gold)"/><rect x="2.5" y="3.3" width="5" height="3.5" fill="none" stroke="var(--teal)" stroke-width=".8"/><path d="M2.5 3.3L5 5.3l2.5-2" fill="none" stroke="var(--teal)" stroke-width=".8"/></svg>Kontakt@quirbalt-marketing.de</li>
    <li class="web"><svg class="dot" viewBox="0 0 10 10" aria-hidden="true"><circle cx="5" cy="5" r="5" fill="var(--gold)"/><circle cx="5" cy="5" r="3" fill="none" stroke="var(--teal)" stroke-width=".7"/><path d="M2 5h6M5 2c-1.4 2-1.4 4 0 6M5 2c1.4 2 1.4 4 0 6" fill="none" stroke="var(--teal)" stroke-width=".6"/></svg>www.quirbalt-marketing.de</li>
  </ul>
</section>

</body>
</html>
```